Varga Lillas Physiotherapy Business Card Vienna

We need a business card design for a newly created Physiotherapy company based in Vienna Austria.
We seek a simple, modern, minimalist design without too much color variation. The font should look young/fresh, but definitely not childish or so. Since we are a starting Business, we currently haven't got a logo, if you feel like a logo would fit your design, feel free to use one, but it's not necessary.
Target Market(s)
Healthcare, young and elderly people with mobility issues
Industry/Entity Type
Health And Wellness
Contact Information for Business Card
Name: Lilla Varga
Title description: Physiotherapist
Phone num: +43 664 5290 4816
e-mail: lilla.praxis@brelomail.com
Colors
Designer to choose colors to be used in the design.
Requirements
Must have
- Final design language must be in German, basically, the Title Description needs to be "Physiotherapeutin" the other details remain as in the English Language.
Nice to have
- Simple, modern, minimalist design
Should not have
- too many colors, Obvious use of a skeleton, skull, spline

```html
<!DOCTYPE html>
<html lang="de">
<head>
<meta charset="utf-8">
<title>Lilla Varga – Physiotherapeutin</title>
<link rel="stylesheet" href="https://fonts.googleapis.com/css2?family=Jost:wght@400&display=swap">
<style>
  :root {
    --backdrop: #b0aeb4;
    --slate: #4f586f;
    --paper: #edf1fa;
    --name-ink: #eef2fb;
    --label-ink: #a8a8b2;
  }
  * { margin: 0; padding: 0; box-sizing: border-box; }
  html, body {
    width: 1200px;
    height: 880px;
    overflow: hidden;
    background: var(--backdrop);
    font-family: "Jost", "Helvetica Neue", Arial, sans-serif;
  }
  .card {
    position: absolute;
    left: 216px;
    top: 192px;
    width: 768px;
    height: 496px;
    background: var(--paper);
    overflow: hidden;
  }
  .name-panel {
    position: absolute;
    left: 0;
    top: 0;
    width: 280px;
    height: 100%;
    background: var(--slate);
  }
  .name {
    position: absolute;
    color: var(--name-ink);
    font-size: 51px;
    font-weight: 400;
    line-height: 1;
    white-space: nowrap;
  }
  .name--first { left: 48px; top: 110px; }
  .name--last { left: 124px; top: 165px; }
  .job-title {
    position: absolute;
    left: 486px;
    top: 55px;
    font-size: 24px;
    letter-spacing: 1.6px;
    color: var(--slate);
    line-height: 1;
    white-space: nowrap;
  }
  .contact {
    position: absolute;
    left: 280px;
    top: 262px;
    display: grid;
    grid-template-columns: 108px auto;
    column-gap: 22px;
    row-gap: 14px;
    font-size: 29px;
    line-height: 31px;
    white-space: nowrap;
  }
  .contact__label {
    color: var(--label-ink);
    text-align: right;
  }
  .contact__value { color: var(--slate); }
</style>
</head>
<body>
  <section class="card">
    <div class="name-panel">
      <span class="name name--first">Lilla</span>
      <span class="name name--last">Varga</span>
    </div>
    <p class="job-title">Physiotherapeutin</p>
    <dl class="contact">
      <dt class="contact__label">tel</dt>
      <dd class="contact__value">+43 664 5290 4816</dd>
      <dt class="contact__label">e-mail</dt>
      <dd class="contact__value">lilla.praxis@brelomail.com</dd>
    </dl>
  </section>
</body>
</html>
```